Real Estate Broker specializing in investment property needs business card

Would like to use a tag line for my company, Larkmoor Keys LLC (Right now I use Larkmoor Keys - For Real Estate Needs). I you have a more creative tag line it can be used because this is a new company.
We focus on Investment Acquisition Deals; Provide Custom Marketing Strategies for Sellers; Provide Pre Listinging Value Opportunities for Buyers.
Would like a call to action, but I do not want it to look too cluttered
I would like space to be available for writing on.
I prefer vertical business cards, but it could be horizontal on one or both sides. In fact if you can create a shape other than rectangle or a cut in the rectangle that makes it memorable, relevant to real estate, yet practical...(it will be kept) that would be of value.
If you have experience with business cards please feel free to suggest the paper type, size.

Target Market(s)

Investors, Neighbors, Friends... anyone who buys or would like to sell their residence

Industry/Entity Type

Real Estate

Contact Information for Business Card

The challenge is to incorporate a logo design of the Managing Brokerage Company, Tiller's Circle, and try to brand my company, LarkmoorKeys LLC. LarkmoorKeys LLC could work under another managing broker but the services and contact information would remain the same.

Font styles to use
Serif

Colors

Designer to choose colors to be used in the design.

Requirements
Must have
• Real estate company named Larkmoor Keys has to incorporate the logo of the managing broker company, Tillers Circle (see attached) into design of business card. (It is not a design for a logo I prefer but I need to use it. Size does not matter).
• Must also have my name, phone number and email address. (No website address yet)
• Just a few of the services we provide include
• We facilitate Investment Acquisition Deals; Provide Custom Marketing Strategies for Sellers; Provide Pre Listinging Value Opportunities for Buyers.
Nice to have
• Would like to use a tag line for my company, Larkmoor Keys LLC (Right now I use Larkmoor Keys - For Real Estate Needs). If you have a more creative tag line it can be used because this is a new company.
• Space to write information on, so they keep the card such as an appointment time to sit down and determine their needs
• A call to action maybe after the services? Or on the back of the card where it is blank.
• Larkmoor Keys does not have a logo, If you think a logo for Tillers Circle and a logo for LarkmoorKeys LLC can work, then please incorporate it into the business card.
Should not have
• Clutter
• Do not like comic style designs; prefer a sophisticated look and texture.

```html
<!DOCTYPE html>
<html lang="en">
<head>
<meta charset="utf-8">
<title>Larkmoor Keys LLC – Business Card</title>
<link rel="stylesheet" href="https://fonts.googleapis.com/css2?family=Cinzel:wght@400;500&family=Lato:wght@400&display=swap">
<style>
  :root {
    --navy: #0b3a78;
    --slate: #6b6b6b;
    --ink: #2a2a2a;
    --rule: #b9b9b9;
    --paper: #ffffff;
    --backdrop: #2f2f2f;
  }
  * { margin: 0; padding: 0; box-sizing: border-box; }
  html, body { width: 1200px; height: 1200px; overflow: hidden; }
  body { background: var(--backdrop); position: relative; font-family: "Lato", sans-serif; color: var(--ink); }

  .card { position: absolute; top: 310px; height: 594px; background: var(--paper); overflow: hidden; text-align: center; }
  .card--front { left: 234px; width: 364px; }
  .card--back { left: 627px; width: 369px; }

  .brand-mark { position: absolute; left: 162px; top: 398px; width: 40px; height: 40px; border-radius: 50%; background: var(--navy); }
  .card--front .brand-mark { top: 88px; }
  .brand-name { position: absolute; top: 176px; left: 0; right: 0; font-family: "Cinzel", serif; font-size: 25px; color: var(--navy); letter-spacing: 0.5px; }
  .brand-tagline { position: absolute; top: 207px; left: 0; right: 0; font-family: "Lato", sans-serif; font-size: 12px; letter-spacing: 4.2px; color: var(--slate); }

  .person-name { position: absolute; top: 287px; left: 0; right: 0; font-family: "Cinzel", serif; font-size: 24px; color: var(--navy); }
  .person-name .surname { color: var(--slate); }
  .person-role { position: absolute; top: 313px; left: 0; right: 0; font-size: 17px; color: var(--slate); }

  .rule { position: absolute; height: 1px; background: var(--rule); }
  .card--front .rule { left: 91px; width: 181px; }
  .contact { position: absolute; left: 0; right: 0; font-size: 17px; line-height: 22px; color: var(--ink); }
  .contact--direct { top: 351px; }
  .contact--address { top: 416px; }

  .footer-band { position: absolute; left: 0; right: 0; bottom: 0; height: 62px; background: var(--navy); }
  .broker-plate { position: absolute; left: 86px; top: 490px; width: 192px; height: 80px; border-radius: 50%; background: var(--paper); display: flex; align-items: center; justify-content: center; }
  .broker-name { font-family: "Lato", sans-serif; font-size: 20px; color: var(--navy); }

  .back-banner { position: absolute; top: 0; left: 0; right: 0; height: 215px; background: linear-gradient(90deg, var(--navy) 0 52%, var(--slate) 52% 100%); }
  .services { position: absolute; top: 235px; left: 0; right: 0; font-size: 17px; line-height: 22px; color: var(--ink); }
  .services p { margin-bottom: 5px; }
  .notes .rule { left: 42px; width: 285px; }
</style>
</head>
<body>
  <section class="card card--front">
    <span class="brand-mark"></span>
    <div class="brand-name">Larkmoor Keys LLC</div>
    <div class="brand-tagline">FOR REAL ESTATE NEEDS</div>

    <div class="person-name">MARCUS <span class="surname">WHITFIELD</span></div>
    <div class="person-role">Managing Director</div>

    <div class="rule" style="top:343px"></div>
    <div class="contact contact--direct">044-987 650 312<br>hello@larkmoorkeys.com</div>
    <div class="rule" style="top:406px"></div>
    <div class="contact contact--address">218, Alder Row Lane,<br>45810,Country Name</div>

    <div class="footer-band"></div>
    <div class="broker-plate"><span class="broker-name">Tillers Circle</span></div>
  </section>

  <section class="card card--back">
    <div class="back-banner" role="img" aria-label="Larkmoor Keys brand banner in navy and slate"></div>
    <div class="services">
      <p>We facilitate Investment<br>Acquisition Deals</p>
      <p>Provide Custom Marketing<br>Strategies for Sellers</p>
      <p>Provide Pre Listinging Value<br>Opportunities for Buyers</p>
    </div>
    <div class="notes">
      <div class="rule" style="top:408px"></div>
      <div class="rule" style="top:449px"></div>
      <div class="rule" style="top:493px"></div>
      <div class="rule" style="top:538px"></div>
    </div>
  </section>
</body>
</html>
```